Trade Alert Service needs Youtube thumbnail / channel design

I'm about to set up a Youtube channel which gives real-time trade alerts to earn passive income. I'm looking for a Youtube channel design to include thumbnail and other associated visuals for the channel.
The trade alerts will be focused around selling cash-secured put options on US equities, and directed at people who want investing advice / tips for getting out of the rat race. I'd like the theme to be somewhat serious / credible, without too many eye-popping neon colours like all the other cheap trade alert videos / day trading videos on Youtube. Happy for you to use your experience if you think otherwise though, as you're the designer, not me!

Target Market(s)

Option Traders, Value Investors, People who want passive income

Industry/Entity Type

Finance

Logo Text

Bramblewick Quarter Guild

Requirements
Must have
• All relevant Youtube visuals so that I can upload them to the Youtube channel - all visuals required by Youtube Studio upload within the channel creation page.
A logo so that I can append it to Powerpoint presentations
Nice to have
• A blank Powerpoint slide template showing the logo would be great in chosen colour scheme

```html
<!DOCTYPE html>
<html lang="en">
<head>
<meta charset="utf-8">
<title>Bramblewick Quarter Guild – Thumbnail</title>
<link href="https://fonts.googleapis.com/css2?family=Exo+2:wght@800;900&display=swap" rel="stylesheet">
<style>
  :root {
    --blue-deep: #1d3cbf;
    --blue-mid: #2a4fcc;
    --blue-light: #3d5fd6;
    --accent-blue: #2a8cff;
    --white: #ffffff;
  }
  * { margin: 0; padding: 0; box-sizing: border-box; }
  html, body {
    width: 1200px;
    height: 675px;
    overflow: hidden;
    background: var(--blue-mid);
  }
  .thumbnail {
    position: relative;
    width: 1200px;
    height: 675px;
    overflow: hidden;
  }
  .photo-backdrop {
    position: absolute;
    inset: 0;
    background:
      radial-gradient(ellipse 45% 55% at 52% 50%, rgba(90,120,225,0.35), transparent 70%),
      linear-gradient(100deg, var(--blue-deep) 0%, var(--blue-mid) 45%, var(--blue-light) 100%);
  }
  .title-block {
    position: absolute;
    left: 50%;
    top: 50%;
    transform: translate(-50%, -50%);
    display: flex;
    flex-direction: column;
    align-items: flex-start;
    font-family: "Exo 2", sans-serif;
    font-weight: 900;
    text-transform: uppercase;
    color: var(--white);
    line-height: 1;
  }
  .title-highlight {
    background: var(--white);
    color: var(--accent-blue);
    font-size: 50px;
    padding: 2px 8px 4px;
    letter-spacing: -0.5px;
    margin-bottom: 10px;
  }
  .title-line {
    font-size: 92px;
    letter-spacing: -1px;
    line-height: 0.82;
    margin-bottom: 10px;
  }
</style>
</head>
<body>
  <main class="thumbnail">
    <div class="photo-backdrop" role="img" aria-label="Photo of a person holding fanned-out US dollar bills in both hands, tinted blue"></div>
    <h1 class="title-block">
      <span class="title-highlight">Bramblewick</span>
      <span class="title-line">Quarter</span>
      <span class="title-line">Guild</span>
    </h1>
  </main>
</body>
</html>
```